Info Graphic about Maple Orchard Restaurant

This info graphic should detail all releavent details about Maple Orchard, such as opening hours, accepted payment methods, home delivery areas etc. please refer attached word document for details.

Also attached a pdf with old info graphic.

IMPORTANT:. Given there is lot of text, I expect the designer to make this interesting. This will be printed in A1 and also A4
Also, I need this in both Portrait and landscape designs.

Industry/Entity Type

Hospitality

Font styles to use
Serif
Sans Serif
Decorative
Script
Other font styles liked:
• I let designer choose

Colors

Designer to choose colors to be used in the design.

Requirements
Must have
• Refer attached word doc
Nice to have
• Refer attached word doc
Should not have
• Refer attached word doc

```html
<!DOCTYPE html>
<html lang="en">
<head>
<meta charset="utf-8">
<title>Maple Orchard Indian Restaurant – Info Sheet</title>
<link href="https://fonts.googleapis.com/css2?family=Rye&family=Montserrat:wght@300;400;600;700&display=swap" rel="stylesheet">
<style>
:root{
  --red:#c1212b;
  --red-soft:#e29a9a;
  --cream:#fbf0cf;
  --cream-band:#f8efcf;
  --ink:#2b2b2b;
  --text:#4a4a4a;
  --white:#ffffff;
}
*{box-sizing:border-box;margin:0;padding:0}
html,body{width:927px;height:1200px;overflow:hidden;background:var(--white)}
body{font-family:"Montserrat",sans-serif;color:var(--text);position:relative}
.abs{position:absolute}

/* header */
.header{left:0;top:0;width:927px;height:136px;background:var(--cream);border-bottom:4px solid var(--red)}
.header-art{left:26px;top:14px;width:76px;height:106px;border-radius:40% 40% 20% 20%;background:linear-gradient(90deg,#d5231f,#f07a1d,#f6b21f,#9bb72c)}
.title{left:118px;top:30px;width:790px;text-align:center;font-family:"Rye",serif;font-size:39px;font-weight:400;color:var(--red);white-space:nowrap}
.tagline{left:118px;top:88px;width:790px;text-align:center;font-size:19px;font-weight:300;color:var(--red);white-space:nowrap}

/* hours */
.hours{left:34px;top:160px;width:514px;height:358px;border:3px solid var(--red);border-radius:3px}
.hours-head{left:58px;top:176px;display:flex;align-items:center;gap:10px;font-weight:700;color:var(--red);font-size:16px}
.hours-rule{left:170px;top:224px;width:370px;height:4px;background:var(--red-soft);border-radius:2px}
.hours-table{left:58px;top:244px;width:460px;border-collapse:collapse;font-size:14.5px;color:var(--text)}
.hours-table th{text-align:left;font-weight:700;color:var(--ink);height:27px}
.hours-table td{height:27.2px}
.hours-table .c{text-align:center}
.buffet{left:80px;top:465px;width:420px;text-align:center;font-size:14.5px;line-height:1.25}

/* owner */
.owner{left:606px;top:168px;width:262px;height:76px;background:var(--red);border-radius:8px;color:var(--white);padding:8px 16px}
.owner-name{font-weight:700;font-size:17px;margin-bottom:4px}
.owner-line{display:flex;align-items:center;gap:9px;font-size:12px;line-height:21px}
.owner-badge{left:802px;top:156px;width:100px;height:100px;border-radius:50%;background:var(--red)}

/* registration */
.reg-icon{left:608px;top:266px}
.reg-title{left:660px;top:279px;font-weight:700;color:var(--red);font-size:17px}
.reg-box{left:614px;top:296px;width:280px;height:210px;border:3px solid var(--red);border-left:none;border-top:none}
.reg-text{left:630px;top:326px;font-size:13.6px;line-height:21.2px;color:var(--text)}
.reg-text b{color:var(--ink)}

/* band */
.band{left:32px;top:538px;width:862px;height:138px;background:var(--cream-band)}
.band-block{top:548px;font-size:13.3px;line-height:19.7px}
.band-block h3{font-size:16px;color:var(--red);font-weight:700;line-height:20px}

/* lower sections */
.sec h3{font-size:16px;color:var(--red);font-weight:700;line-height:22px}
.sec p,.sec li{font-size:14.5px;line-height:21.2px}
.divider{height:2px;background:var(--red)}
.divider::before,.divider::after{content:"";position:absolute;top:-4px;width:10px;height:10px;border-radius:50%;background:var(--red)}
.divider::before{left:-4px}.divider::after{right:-4px}
.divider.grey{background:#999}
.divider.grey::before{background:#999}
.divider.grey::after{display:none}
.rules li{list-style:none;position:relative;padding-left:28px}
.rules li::before{content:"•";position:absolute;left:0}
.map{left:664px;top:694px;width:263px;height:264px;background:linear-gradient(135deg,#e4ebe3,#eef0ec 55%,#dfe8dc)}
.delivery-note{left:428px;top:910px;font-style:italic;font-size:14.5px;line-height:19px}

/* footer */
.foot-left{left:0;top:1075px;width:498px;height:98px;background:var(--cream)}
.foot-right{left:498px;top:1075px;width:429px;height:98px;background:var(--red)}
.services{left:116px;top:1093px;font-size:14.5px;line-height:21.2px;width:375px;white-space:nowrap}
.services b{color:var(--red)}
.warn-title{left:582px;top:1089px;font-size:21px;font-weight:600;letter-spacing:.5px;color:var(--white)}
.warn-text{left:582px;top:1116px;font-size:13.6px;font-weight:700;line-height:21px;color:var(--white)}
</style>
</head>
<body>

<header>
  <div class="abs header"></div>
  <div class="abs header-art" role="img" aria-label="Illustration of red, orange and green chilli peppers"></div>
  <h1 class="abs title">Maple Orchard Indian Restaurant</h1>
  <p class="abs tagline">Your best Indian Restaurant in Perth's Northern suburbs</p>
</header>

<section>
  <div class="abs hours"></div>
  <div class="abs hours-head">
    <svg width="40" height="40" viewBox="0 0 40 40"><circle cx="20" cy="20" r="17" fill="none" stroke="#c1212b" stroke-width="2.5"/><path d="M20 9v11l7 5" fill="none" stroke="#c1212b" stroke-width="2.5" stroke-linecap="round"/></svg>
    Opening Hours
  </div>
  <div class="abs hours-rule"></div>
  <svg class="abs" style="left:228px;top:200px" width="40" height="32" viewBox="0 0 40 32"><path d="M8 20a12 12 0 0 1 24 0" fill="none" stroke="#c1212b" stroke-width="2.5"/><path d="M20 2v5M6 8l3 3M34 8l-3 3M2 20h5M33 20h5M4 26h32M9 31h22" stroke="#c1212b" stroke-width="2.2" stroke-linecap="round"/></svg>
  <svg class="abs" style="left:408px;top:196px" width="40" height="36" viewBox="0 0 40 36"><path d="M12 2l3 8h8l-6 5 2 8-7-5-7 5 2-8-6-5h8z" fill="#c1212b"/><path d="M27 18l2 5h5l-4 3 1 5-4-3-4 3 1-5-4-3h5z" fill="#c1212b"/><path d="M28 6l3 2 3-2M32 12l3 2 3-2" fill="none" stroke="#c1212b" stroke-width="1.6"/></svg>
  <table class="abs hours-table">
    <tr><th>Day</th><th class="c">Morning</th><th class="c">Evening</th></tr>
    <tr><td>Monday</td><td class="c">11:30AM – 2:30PM</td><td class="c">5:00PM – 9:00PM</td></tr>
    <tr><td>Tuesday</td><td class="c">11:30AM – 2:30PM</td><td class="c">5:00PM – 9:00PM</td></tr>
    <tr><td>Wednesday</td><td class="c">11:30AM – 2:30PM</td><td class="c">5:00PM – 9:00PM</td></tr>
    <tr><td>Thursday</td><td class="c">11:30AM – 2:30PM</td><td class="c">5:00PM – 9:00PM</td></tr>
    <tr><td>Friday</td><td class="c">11:30AM – 2:30PM</td><td class="c">5:00PM – 9:00PM</td></tr>
    <tr><td>Saturday</td><td class="c">10:30AM – 2:30PM</td><td class="c">5:00PM – 9:00PM</td></tr>
    <tr><td>Sunday</td><td class="c">10:30AM – 2:30PM</td><td class="c">5:00PM – 9:00PM</td></tr>
  </table>
  <p class="abs buffet">Dinner Buffet is available only from<br>Mon-Thu from 5:30PM – 8:30PM</p>
</section>

<section>
  <div class="abs owner-badge"></div>
  <div class="abs owner">
    <div class="owner-name">Rina Kestrel</div>
    <div class="owner-line"><svg width="10" height="16" viewBox="0 0 10 16"><rect x="1" y="1" width="8" height="14" rx="1.5" fill="none" stroke="#fff" stroke-width="1.5"/></svg>0400123456</div>
    <div class="owner-line"><svg width="16" height="11" viewBox="0 0 16 11"><rect x="1" y="1" width="14" height="9" fill="none" stroke="#fff" stroke-width="1.4"/><path d="M1 1l7 5 7-5" fill="none" stroke="#fff" stroke-width="1.4"/></svg>rina@mapleorchard.com.au</div>
  </div>

  <svg class="abs reg-icon" width="42" height="50" viewBox="0 0 42 50"><rect x="2" y="2" width="36" height="44" fill="none" stroke="#c1212b" stroke-width="2.5"/><path d="M9 12h22M9 19h22M9 26h14" stroke="#c1212b" stroke-width="2.2"/><circle cx="28" cy="36" r="7" fill="#c1212b"/><path d="M25 36l2 2 4-4" fill="none" stroke="#fff" stroke-width="1.8"/></svg>
  <div class="abs reg-box"></div>
  <h2 class="abs reg-title">Registration Details</h2>
  <p class="abs reg-text"><b>Birchwood House Pty Ltd</b><br><b>T/A Maple Orchard Restaurant</b><br>ABN: 12 345 678 901<br>Shop 7-8, 412 Harbour Ave.,<br>Lakeview, WA 6000<br>Australia<br>Ph: 08 9000 1234<br>Email: admin@mapleorchard.com.au</p>
</section>

<section>
  <div class="abs band"></div>
  <svg class="abs" style="left:46px;top:562px" width="72" height="70" viewBox="0 0 72 70"><path d="M4 50l22-10 10 14-22 12z" fill="#c1212b"/><rect x="24" y="8" width="42" height="30" rx="4" transform="rotate(-18 45 23)" fill="#c1212b"/><rect x="32" y="18" width="14" height="9" fill="#fff" transform="rotate(-18 45 23)"/></svg>
  <div class="abs band-block" style="left:134px">
    <h3>Payment Methods:</h3>
    We accept cash, all Australian EFTPOS,<br>Debit and Credit Cards.<br>We accept Amber Card, Orbit Card –<br>A surcharge of 2.8% apply.<br>We DO NOT accept Supper Club
  </div>
  <svg class="abs" style="left:472px;top:562px" width="70" height="70" viewBox="0 0 70 70"><path d="M4 44L44 4l8 8a6 6 0 0 0 8 8l6 6-40 40-6-6a6 6 0 0 0-8-8z" fill="#c1212b"/><text x="30" y="44" font-family="Montserrat,sans-serif" font-weight="700" font-size="18" fill="#fff" transform="rotate(-45 35 38)">%</text></svg>
  <div class="abs band-block" style="left:562px">
    <h3>Discount Vouchers:</h3>
    We accept Leisure Book Vouchers<br>and Maple Orchard supplied Discount vouchers.<br>Leisure Vouchers are eligible only<br>for Dine-In.
  </div>
</section>

<section>
  <svg class="abs" style="left:26px;top:718px" width="80" height="36" viewBox="0 0 80 36"><rect x="14" y="6" width="52" height="8" fill="#c1212b"/><rect x="30" y="2" width="20" height="6" fill="none" stroke="#c1212b" stroke-width="2"/><path d="M24 14v20M56 14v20M4 8v26M4 24h12v10M76 8v26M76 24H64v10" stroke="#c1212b" stroke-width="3" fill="none"/></svg>
  <div class="abs sec" style="left:118px;top:706px;width:280px">
    <h3>Book your Table</h3>
    <p>Please visit<br>www.mapleorchard.com.au to<br>book your table or contact us<br>on 08 9000 1234</p>
  </div>
  <div class="abs divider" style="left:32px;top:822px;width:314px"></div>

  <svg class="abs" style="left:44px;top:830px" width="44" height="60" viewBox="0 0 44 60"><path d="M4 14h14c0 10-3 14-7 14s-7-4-7-14z" fill="none" stroke="#c1212b" stroke-width="2"/><path d="M11 28v20M5 48h12" stroke="#c1212b" stroke-width="2"/><path d="M30 2h6v12c4 3 6 6 6 12v30H24V26c0-6 2-9 6-12z" fill="#c1212b"/></svg>
  <div class="abs sec" style="left:118px;top:830px;width:280px">
    <h3>BYO</h3>
    <p>BYO allowed – only for Wine.<br>Charges per bottle apply</p>
  </div>
  <div class="abs divider" style="left:32px;top:918px;width:314px"></div>

  <svg class="abs" style="left:40px;top:934px" width="48" height="56" viewBox="0 0 48 56"><path d="M2 2h32l12 12v40H2z" fill="none" stroke="#c1212b" stroke-width="2.5"/><path d="M12 22l12-10 12 10v12H12z" fill="#c1212b"/><path d="M10 42h28M10 48h20" stroke="#c1212b" stroke-width="2.2"/></svg>
  <div class="abs sec" style="left:118px;top:928px;width:280px">
    <h3>House Rules</h3>
    <ul class="rules">
      <li>Prices are inclusive of GST</li>
      <li>Prices are subject to change without notice</li>
      <li>Outside Food and Beverages (except WINE) are not allowed</li>
    </ul>
  </div>

  <svg class="abs" style="left:386px;top:710px" width="44" height="42" viewBox="0 0 44 42"><rect x="2" y="2" width="36" height="30" fill="none" stroke="#c1212b" stroke-width="2"/><path d="M2 9h36M8 16h12M8 22h12M24 16h8" stroke="#c1212b" stroke-width="2"/><path d="M30 22l10 10-4 1 3 5-2 1-3-5-3 3z" fill="#fff" stroke="#c1212b" stroke-width="1.6"/></svg>
  <div class="abs sec" style="left:446px;top:706px;width:220px">
    <h3>Order Online</h3>
    <p>www.mapleorchard.com.au<br>www.dishdrop.com.au<br>www.platerun.com.au<br>www.quickbite.com.au</p>
  </div>
  <div class="abs divider" style="left:392px;top:822px;width:272px"></div>

  <svg class="abs" style="left:386px;top:830px" width="46" height="40" viewBox="0 0 46 40"><circle cx="10" cy="32" r="6" fill="none" stroke="#c1212b" stroke-width="3"/><circle cx="36" cy="32" r="6" fill="none" stroke="#c1212b" stroke-width="3"/><rect x="2" y="12" width="14" height="12" fill="#c1212b"/><path d="M16 24h18l4-10" stroke="#c1212b" stroke-width="4" fill="none"/><circle cx="28" cy="5" r="4" fill="#c1212b"/><path d="M24 10l4 12" stroke="#c1212b" stroke-width="4"/></svg>
  <div class="abs sec" style="left:446px;top:830px;width:220px">
    <h3>Home/Office Delivery:</h3>
    <p>We deliver to following<br>suburbs <svg width="9" height="12" viewBox="0 0 9 12"><path d="M4.5 0a4.5 4.5 0 0 1 4.5 4.5C9 8 4.5 12 4.5 12S0 8 0 4.5A4.5 4.5 0 0 1 4.5 0z" fill="#c1212b"/><circle cx="4.5" cy="4.5" r="1.6" fill="#fff"/></svg></p>
  </div>
  <div class="abs divider grey" style="left:392px;top:904px;width:272px;height:1.5px"></div>
  <p class="abs delivery-note">Delivery Charges $5 and<br>minimum order value $30</p>

  <div class="abs map" role="img" aria-label="Street map of Perth's northern suburbs with pins marking the delivery areas and the restaurant location"></div>

  <svg class="abs" style="left:498px;top:974px" width="58" height="58" viewBox="0 0 58 58"><path d="M6 6l2-4 2 4M16 6l2-4 2 4M26 6l2-4 2 4M36 6l2-4 2 4M46 6l2-4 2 4" stroke="#c1212b" stroke-width="1.5" fill="none"/><rect x="8" y="10" width="42" height="46" fill="none" stroke="#c1212b" stroke-width="2.5"/><path d="M14 18h6M26 18h6M38 18h6M14 28h6M26 28h6M38 28h6M14 38h6M38 38h6" stroke="#c1212b" stroke-width="3"/><rect x="24" y="40" width="10" height="16" fill="#c1212b"/></svg>
  <div class="abs sec" style="left:580px;top:974px;width:340px">
    <h3>Facilities</h3>
    <p>Wheel chair access || Disabled Toilet inside Baby Changer table || High rise tables for babies || Music System</p>
  </div>
</section>

<footer>
  <div class="abs foot-left"></div>
  <svg class="abs" style="left:40px;top:1096px" width="56" height="54" viewBox="0 0 56 54"><circle cx="14" cy="10" r="6" fill="none" stroke="#c1212b" stroke-width="2"/><path d="M4 34v-12a10 10 0 0 1 20 0v12" fill="none" stroke="#c1212b" stroke-width="2"/><rect x="28" y="8" width="24" height="16" fill="none" stroke="#c1212b" stroke-width="2"/><path d="M2 34h52v6H2zM8 40v12M48 40v12M20 44h16v8H20z" fill="none" stroke="#c1212b" stroke-width="2"/></svg>
  <p class="abs services"><b>Services:</b> Functions/Parties | Bulk Cooking<br>Catering | Special Orders | Party Orders<br>Business Meetings | Seminars/Presentations</p>

  <div class="abs foot-right"></div>
  <svg class="abs" style="left:512px;top:1096px" width="62" height="54" viewBox="0 0 62 54"><path d="M31 3L59 51H3z" fill="#f6b21f" stroke="#f6b21f" stroke-width="4" stroke-linejoin="round"/><path d="M31 18v18" stroke="#c1212b" stroke-width="5" stroke-linecap="round"/><circle cx="31" cy="44" r="3" fill="#c1212b"/></svg>
  <h2 class="abs warn-title">WARNING</h2>
  <p class="abs warn-text">Please inform wait staff for any allergies.<br>Food consumed at your own risk.</p>
</footer>

</body>
</html>
```